依頼詳細
デザインをお願いする当サイトのトップページの役割は、
・当該部門の抽象的イメージの表現
・各種コンテンツ(製品情報、ブログ記事)のポータル的機能
の2つを主軸に据えようと考えています。

デザインの条件として、
・サイトロゴはこちから指定したものを使用する。
・レスポンシブデザインを適用する。
とさせて頂きます。ついては、

開発したアプリ、サービス等の周知、蓄積した技術情報等の発信を行うためにWebサイトとして見栄えがする、
・ページ全体、および個々の要素の配色
・ボーダー、シャドウのデザイン
・各要素の質感
のデザインをご提案頂きたいです。

現在、こちらで添付のようなページレイアウトを検討していますが、あくまで案ですので、レイアウトも含めたデザインをご提案いただいても構いません。
ページ数
1ページ
希望イメージ
シンプル 複雑
単色 カラフル
暗い 明るい
日常 高級
遊び心 厳粛
未来的 伝統的
女性的 男性的
希望する色
ロゴのカラーバリエーションのいずれかにマッチする配色でお願いします。
納品ファイル
• 高解像度JPG (.jpg)
• イラストレーター形式 (.ai)
• フォトショップ形式 (.psd)
• PNG形式 (.png)
補足説明
ロゴには、カラーバリエーションがありますので、サイト全体の配色に合うものを
適宜選択していただければと思います。
〆切を延長させて頂きます。
■ 選んだ理由

シンプルでわかりやすいデザインがサイトにマッチすると思いました。

■ 提案者全員のお礼・コメント

たくさんのご提案をありがとうございます。
今後ともよろしくお願いします。

```html
<!DOCTYPE html>
<html lang="ja">
<head>
<meta charset="utf-8">
<title>Kairo Labs</title>
<link rel="stylesheet" href="https://fonts.googleapis.com/css2?family=Nunito:wght@400;600;700&family=Noto+Sans+JP:wght@400;500&display=swap">
<style>
:root{
  --teal:#2bb7b0;
  --teal-soft:#a6e3df;
  --teal-band:#8fdad5;
  --ink:#3c4a52;
  --muted:#7b8a91;
  --page:#eef2f4;
  --white:#ffffff;
  --hero-a:#1e4fa3;
  --hero-b:#0f2f78;
}
*{margin:0;padding:0;box-sizing:border-box}
html,body{width:877px;height:1200px;overflow:hidden}
body{background:var(--white);font-family:"Nunito","Noto Sans JP",sans-serif;color:var(--ink);position:relative}
.site-header{position:absolute;left:0;top:0;width:877px;height:46px;background:var(--white);border-top:3px solid var(--teal)}
.brand{position:absolute;display:flex;align-items:center;gap:6px;font-weight:700;color:var(--teal);font-family:"Nunito",sans-serif}
.brand-dot{border-radius:50%;background:var(--teal)}
.site-header .brand{left:78px;top:9px;font-size:22px}
.site-header .brand-dot{width:18px;height:18px}
.main-nav{position:absolute;right:180px;top:8px;display:flex;gap:18px}
.main-nav a{font-size:10px;color:var(--muted);text-decoration:none;display:flex;flex-direction:column;align-items:center;gap:4px}
.main-nav a::after{content:"";width:9px;height:9px;border-radius:50%;background:var(--teal-soft)}
.main-nav a.current{color:var(--teal)}
.main-nav a.current::after{background:var(--teal)}
.hero{position:absolute;left:78px;top:48px;width:722px;height:282px;background:linear-gradient(100deg,#9fb6c9 0%,#5c7fa8 30%,var(--hero-a) 55%,var(--hero-b) 100%);overflow:hidden}
.hero-photo{position:absolute;left:0;top:0;width:430px;height:282px;background:linear-gradient(135deg,#c9d6df,#7d96ad 60%,rgba(30,79,163,0))}
.hero .brand{left:520px;top:92px;font-size:30px;color:var(--white)}
.hero .brand-dot{width:26px;height:26px;background:var(--white)}
.hero-copy{position:absolute;left:520px;top:150px;width:190px;font-size:9px;line-height:1.35;color:var(--white)}
.products{position:absolute;left:0;top:330px;width:877px;height:218px;background:var(--page)}
.section-title{position:absolute;left:0;width:877px;text-align:center;font-weight:700;font-size:14px;display:flex;justify-content:center;align-items:center;gap:6px}
.section-title::before{content:"";width:12px;height:12px;border-radius:50%;background:var(--teal)}
.section-sub{position:absolute;left:0;width:877px;text-align:center;font-size:8px;color:var(--muted);font-family:"Noto Sans JP",sans-serif}
.product{position:absolute;top:68px;width:172px}
.product-img{height:96px;border-radius:2px}
.product-label{margin-top:6px;padding-left:28px;font-size:10px;font-weight:600;position:relative}
.product-label::before{content:"";position:absolute;left:14px;top:3px;width:10px;height:10px;border-radius:50%;background:var(--teal)}
.product-label span{display:block;font-size:7px;color:var(--muted);font-weight:400;font-family:"Noto Sans JP",sans-serif}
.blog{position:absolute;left:0;top:548px;width:877px;height:470px;background:var(--teal-band)}
.card{position:absolute;width:162px;height:180px;background:var(--white);box-shadow:0 1px 3px rgba(0,0,0,.12)}
.card-img{height:118px}
.card-date{font-size:7px;color:var(--muted);padding:6px 8px 2px}
.card-title{font-size:8px;line-height:1.4;padding:0 8px;font-family:"Noto Sans JP",sans-serif}
.site-footer{position:absolute;left:0;top:1018px;width:877px;height:182px;background:var(--page)}
.site-footer .brand{left:205px;top:40px;flex-direction:column;font-size:18px;gap:4px}
.site-footer .brand-dot{width:34px;height:34px}
.footer-nav{position:absolute;left:345px;top:68px;display:flex;gap:14px;font-size:9px}
.footer-nav a{color:var(--muted);text-decoration:none}
.footer-nav a.current{color:var(--teal)}
.copyright{position:absolute;left:345px;top:92px;font-size:7px;color:var(--muted)}
.social{position:absolute;left:600px;top:63px;display:flex;gap:6px}
.social span{width:18px;height:18px;border-radius:50%;background:var(--white);border:1px solid #d3dbe0}
</style>
</head>
<body>
<header class="site-header">
  <div class="brand"><span class="brand-dot"></span>Kairo Labs</div>
  <nav class="main-nav">
    <a class="current" href="#">Home</a><a href="#">Products</a><a href="#">Blog</a><a href="#">Contact</a>
  </nav>
</header>

<section class="hero">
  <div class="hero-photo" role="img" aria-label="Hands holding a tablet showing a city skyline"></div>
  <div class="brand"><span class="brand-dot"></span>Kairo Labs</div>
  <p class="hero-copy">The 1st state-of-the-art smartphone app<br>WEB site production.<br>This is a provided technical information.<br>It will continue to outgoing towards the future.</p>
</section>

<section class="products">
  <h2 class="section-title" style="top:22px">Products</h2>
  <p class="section-sub" style="top:42px">製品</p>
  <div class="product" style="left:188px">
    <div class="product-img" role="img" aria-label="Rows of smartphones and tablets" style="background:linear-gradient(135deg,#9fc3dc,#3f6f9c)"></div>
    <p class="product-label">Smartphone<span>スマートフォン</span></p>
  </div>
  <div class="product" style="left:352px">
    <div class="product-img" role="img" aria-label="Laptop, tablet and phone on a desk" style="background:linear-gradient(135deg,#e6ecef,#a9b8c2)"></div>
    <p class="product-label">Web Service<span>ウェブサービス</span></p>
  </div>
  <div class="product" style="left:516px">
    <div class="product-img" role="img" aria-label="Hand writing notes beside a coffee cup" style="background:linear-gradient(135deg,#f3f1ec,#c8c2b6)"></div>
    <p class="product-label">Blog<span>ブログ</span></p>
  </div>
</section>

<section class="blog">
  <h2 class="section-title" style="top:36px">Popular blog introduction</h2>
  <p class="section-sub" style="top:56px">人気記事</p>
  <article class="card" style="left:188px;top:80px"><div class="card-img" role="img" aria-label="Smartphones arranged on a table" style="background:linear-gradient(135deg,#dfe6ea,#8798a5)"></div><p class="card-date">2015.05.01</p><p class="card-title">セキュリティー対策で<br>クラウド保存の活用術</p></article>
  <article class="card" style="left:357px;top:80px"><div class="card-img" role="img" aria-label="Flat marketing illustration" style="background:linear-gradient(135deg,#f08a4b,#e8553d)"></div><p class="card-date">2015.05.01</p><p class="card-title">セキュリティー対策で<br>クラウド保存の活用術</p></article>
  <article class="card" style="left:526px;top:80px"><div class="card-img" role="img" aria-label="Laptop on a white desk" style="background:linear-gradient(135deg,#f4f5f6,#c4ccd2)"></div><p class="card-date">2015.05.01</p><p class="card-title">セキュリティー対策で<br>クラウド保存の活用術</p></article>
  <article class="card" style="left:188px;top:275px"><div class="card-img" role="img" aria-label="Business person using a tablet" style="background:linear-gradient(135deg,#c9d2d8,#4e5c68)"></div><p class="card-date">2015.05.01</p><p class="card-title">セキュリティー対策で<br>クラウド保存の活用術</p></article>
  <article class="card" style="left:357px;top:275px"><div class="card-img" role="img" aria-label="Smartphone held near a table" style="background:linear-gradient(135deg,#e9e4dc,#7c7368)"></div><p class="card-date">2015.05.01</p><p class="card-title">セキュリティー対策で<br>クラウド保存の活用術</p></article>
  <article class="card" style="left:526px;top:275px"><div class="card-img" role="img" aria-label="Circuit board close-up" style="background:linear-gradient(135deg,#d9dde0,#6f7a82)"></div><p class="card-date">2015.05.01</p><p class="card-title">セキュリティー対策で<br>クラウド保存の活用術</p></article>
</section>

<footer class="site-footer">
  <div class="brand"><span class="brand-dot"></span>Kairo Labs</div>
  <nav class="footer-nav">
    <a class="current" href="#">Home</a><a href="#">Products</a><a href="#">Blog</a><a href="#">Contact</a><a href="#">Company</a>
  </nav>
  <p class="copyright">Copyright © Kairo Labs. All rights reserved.</p>
  <div class="social"><span></span><span></span><span></span></div>
</footer>
</body>
</html>
```